Vorne - Pop/Rock Album Artwork

Vorne are a London based Rock/Indie band and this is our 2nd album. We require CD cover artwork.
Here is the artwork for our first album: https://www.shopvelto.co.uk/gp/product/Q482KX71Z3?ie=UTF8&*Version*=1&*entries*=0
We like the following attached CD Covers and we are in the same genre music as these bands.
The Album will be called "Glass Ember", the band name "VORNE" should be uppercase. Ideally the name "VORNE" will be designed in such a way that we can use this font on badges and as a Logo itself.
The track listing is:-
1 Unspun
2. Nine Candles
3. Rusty Bell
4. Drifts
5. Harbour
6. Bend a Tide
7. Kites
8. Marbena
9. Past the Gate
10. Pale Ferry
11. Tumble
This project should really just cover the front page of the artwork for a digital CD artwork to be used on Melorack and Plimsy.
Please do listen to our music here: https://wavenook.com/vorne

```html
<!DOCTYPE html>
<html lang="en">
<head>
<meta charset="utf-8">
<title>VORNE – From Glass Ember</title>
<link rel="stylesheet" href="https://fonts.googleapis.com/css2?family=Montserrat:wght@500;700&display=swap">
<style>
  :root {
    --ink: #ffffff;
    --sky-top: #07080a;
    --sky-mid: #14140f;
    --glow: rgba(150, 78, 30, 0.55);
    --field: #1c2a10;
    --field-deep: #0b1206;
  }
  html, body {
    margin: 0;
    padding: 0;
    width: 1200px;
    height: 1200px;
    overflow: hidden;
    background: var(--sky-top);
  }
  .cover {
    position: relative;
    width: 1200px;
    height: 1200px;
    overflow: hidden;
    font-family: "Montserrat", sans-serif;
    color: var(--ink);
  }
  .cover__scene {
    position: absolute;
    inset: 0;
    background:
      radial-gradient(ellipse 520px 180px at 900px 470px, var(--glow), transparent 70%),
      radial-gradient(ellipse 420px 120px at 240px 520px, rgba(90, 70, 50, 0.35), transparent 70%),
      linear-gradient(180deg, var(--sky-top) 0%, var(--sky-mid) 55%, #111108 72%, var(--field) 82%, var(--field-deep) 100%);
  }
  .cover__masthead {
    position: absolute;
    top: 62px;
    left: 0;
    width: 1200px;
    text-align: center;
  }
  .band-name {
    margin: 0;
    font-weight: 700;
    font-size: 170px;
    line-height: 1;
    letter-spacing: 2px;
  }
  .album-title {
    margin: 22px 0 0 0;
    padding-left: 90px;
    font-weight: 500;
    font-size: 25px;
    letter-spacing: 19px;
  }
  .tracklist {
    position: absolute;
    top: 392px;
    left: 0;
    width: 1200px;
    margin: 0;
    padding: 0;
    list-style: none;
    text-align: center;
    font-weight: 500;
    font-size: 58px;
    line-height: 68.4px;
  }
</style>
</head>
<body>
  <main class="cover">
    <div class="cover__scene" role="img" aria-label="Night-time photograph: starry sky with a warm orange glow over a dark wooden barn and a grassy field"></div>

    <header class="cover__masthead">
      <h1 class="band-name">VORNE</h1>
      <p class="album-title">From Glass Ember</p>
    </header>

    <ol class="tracklist">
      <li>1. Unspun</li>
      <li>2. Nine Candles</li>
      <li>3. Rusty Bell</li>
      <li>4. Drifts</li>
      <li>5. Harbour</li>
      <li>6. Bend a Tide</li>
      <li>7. Kites</li>
      <li>8. Marbena</li>
      <li>9. Past the Gate</li>
      <li>10. Pale Ferry</li>
      <li>11. Tumble</li>
    </ol>
  </main>
</body>
</html>
```